Project Brightvale Remedies

We need a business/ logo card design for our company based out of Canada. We will be retailing cannibus products to our customers.
For colors I've found this online : https://www.pallortune.edu/shade-picker-output/?tones=70ff02,ff0270,ff4a02,02e1ff . We especially like the green and blue .
We would like our business card design to communicate modern medicine .

Target Market(s)

males 20-40 years

Industry/Entity Type

Health And Wellness

Contact Information for Business Card

Address is : 482 Marlow Ave E
Toronto, ON K3T 8R2
website: www.brightvaleremedies.com

Font styles to use
Serif

Requirements
Must have
• clear, easy to read logo
Nice to have
• contrasting colors
Should not have
• we want to stay away from marijuana leaf

```html
<!DOCTYPE html>
<html lang="en">
<head>
<meta charset="utf-8">
<title>Brightvale Remedies – Business Card</title>
<link href="https://fonts.googleapis.com/css2?family=Montserrat:wght@500;600;700&display=swap" rel="stylesheet">
<style>
  :root {
    --page-bg: #eef0ee;
    --card-bg: #fbfbfb;
    --brand-green: #8dc63f;
    --brand-blue: #3fa9dc;
    --ink-dark: #555555;
    --ink-light: #9a9a9a;
    --ink-contact: #222222;
    --rule: #222222;
  }
  * { margin: 0; padding: 0; box-sizing: border-box; }
  html, body {
    width: 1200px; height: 1200px; overflow: hidden;
    background: var(--page-bg);
    font-family: "Montserrat", Arial, sans-serif;
  }
  .card {
    position: absolute; left: 40px; top: 280px;
    width: 1120px; height: 640px;
    background: var(--card-bg);
  }
  .brand-mark {
    position: absolute; left: 512px; top: 102px;
    width: 86px; height: 86px;
    border: 4px solid var(--brand-blue); border-radius: 50%;
  }
  .brand-name {
    position: absolute; left: 0; width: 100%; top: 204px;
    text-align: center;
    font-weight: 700; font-size: 46px; letter-spacing: 1px;
    color: var(--brand-green);
  }
  .person {
    position: absolute; right: 654px; top: 380px;
    text-align: right;
  }
  .person-name {
    font-weight: 500; font-size: 44px; letter-spacing: -1px; line-height: 1;
    color: var(--ink-dark);
  }
  .person-name .last { color: var(--ink-light); }
  .person-role {
    margin-top: 14px;
    font-weight: 600; font-size: 24px; letter-spacing: 2px; line-height: 1;
    color: var(--brand-green);
  }
  .divider {
    position: absolute; left: 515px; top: 386px;
    width: 3px; height: 80px; background: var(--rule);
  }
  .contact-list {
    position: absolute; left: 560px; top: 386px;
    list-style: none;
  }
  .contact-item {
    display: flex; align-items: center; gap: 14px;
    height: 27px;
    font-weight: 600; font-size: 16px; letter-spacing: 1px;
    color: var(--ink-contact);
  }
  .contact-icon { width: 20px; height: 20px; fill: var(--brand-blue); flex: none; }
</style>
</head>
<body>
  <main class="card">
    <div class="brand-mark"></div>
    <div class="brand-name">BRIGHTVALE REMEDIES</div>

    <div class="person">
      <div class="person-name">DANA <span class="last">WHITCOMBE</span></div>
      <div class="person-role">PRESIDENT</div>
    </div>

    <div class="divider"></div>

    <ul class="contact-list">
      <li class="contact-item">
        <svg class="contact-icon" viewBox="0 0 24 24" aria-hidden="true"><path d="M6.6 10.8a15 15 0 0 0 6.6 6.6l2.2-2.2a1 1 0 0 1 1-.25 11.4 11.4 0 0 0 3.6.57 1 1 0 0 1 1 1V20a1 1 0 0 1-1 1A17 17 0 0 1 3 4a1 1 0 0 1 1-1h3.5a1 1 0 0 1 1 1c0 1.25.2 2.45.57 3.57a1 1 0 0 1-.25 1z"/></svg>
        <span>+014-672-3851</span>
      </li>
      <li class="contact-item">
        <svg class="contact-icon" viewBox="0 0 24 24" aria-hidden="true"><circle cx="12" cy="12" r="10"/><path d="M2 12h20M12 2c3 3 3 17 0 20M12 2c-3 3-3 17 0 20" stroke="#fff" stroke-width="1.4" fill="none"/></svg>
        <span>www.brightvaleremedies.com</span>
      </li>
      <li class="contact-item">
        <svg class="contact-icon" viewBox="0 0 24 24" aria-hidden="true"><path d="M12 2a7 7 0 0 0-7 7c0 5.2 7 13 7 13s7-7.8 7-13a7 7 0 0 0-7-7zm0 9.5A2.5 2.5 0 1 1 12 6.5a2.5 2.5 0 0 1 0 5z"/></svg>
        <span>482 Marlow Ave E Toronto, ON K3T 8R2</span>
      </li>
    </ul>
  </main>
</body>
</html>
```